Antigen Preservation Bureau

The company will provide a contract research services to stabilize various viruses, viral vectors, and vaccines. It may offer some licensing opportunities for stabilizing technologies. Main area of applications are pharmaceutical, therapeutic, and vaccination field. The company aspires to develop room temperature vaccines for global distribution beyond the current cold chain.

Target Market(s)

pharmaceutical, therapeutic and vaccination fields

Coding

Coded - Design and coding required

Number of Pages Required

4 page

Requirements
Must have
• Incorporate a APB logo, attached at the bottom, on the Web page

```html
<!DOCTYPE html>
<html lang="en">
<head>
<meta charset="utf-8">
<title>Antigen Preservation Bureau</title>
<link rel="stylesheet" href="https://fonts.googleapis.com/css2?family=Oswald:wght@400;500&family=Open+Sans:wght@400;600;700&display=swap">
<style>
:root{
  --green:#8cc63f;
  --green-light:#b5d94a;
  --teal:#2a9d8f;
  --teal-dark:#1f7f75;
  --ink:#2e3a44;
  --muted:#7a858d;
  --footer:#1d2730;
  --footer-bar:#141c22;
  --white:#ffffff;
  --hero-a:#e9efee;
  --hero-b:#c9d6d4;
}
*{box-sizing:border-box;margin:0;padding:0}
html,body{width:1200px;height:2500px;overflow:hidden}
body{font-family:"Open Sans",Arial,sans-serif;color:var(--ink);background:var(--white);position:relative}
.heading{font-family:"Oswald",Arial,sans-serif;font-weight:400;text-transform:uppercase;letter-spacing:1px}

/* header + hero */
.hero{position:absolute;top:0;left:0;width:1200px;height:640px;
  background:linear-gradient(100deg,var(--hero-a) 0%,#dde6e5 45%,var(--hero-b) 100%)}
.hero-photo{position:absolute;right:90px;top:40px;width:420px;height:600px;
  background:linear-gradient(180deg,#d5dedd 0%,#b9c7c6 60%,#aebcbb 100%);border-radius:4px}
.site-header{position:absolute;top:0;left:0;width:1200px;height:110px;display:flex;align-items:center;justify-content:space-between;padding:0 48px}
.brand{display:flex;align-items:center;gap:12px}
.brand-mark{width:34px;height:34px;border-radius:50%;background:var(--teal)}
.brand-name{font-family:"Open Sans",Arial,sans-serif;font-weight:600;font-size:15px;line-height:1.2;color:var(--teal);text-transform:uppercase;letter-spacing:2px;width:170px}
.nav{display:flex;gap:30px;align-items:center;font-size:14px;color:var(--ink)}
.nav-cta{background:var(--green);color:var(--white);width:60px;height:28px;border-radius:14px}
.hero-copy{position:absolute;left:48px;top:330px;width:560px}
.hero-title{font-size:46px;line-height:1.1;color:var(--ink)}
.hero-text{margin-top:18px;font-size:12px;line-height:1.6;color:var(--muted)}
.btn{display:inline-block;font-size:11px;font-weight:600;padding:8px 22px;border-radius:3px;text-transform:uppercase}
.btn-green{background:var(--green);color:var(--white);margin-top:22px}

/* section titles */
.section-title{position:absolute;left:0;width:1200px;text-align:center;font-size:44px;color:var(--ink)}
.section-lead{position:absolute;left:300px;width:600px;text-align:center;font-size:12px;line-height:1.6;color:var(--muted)}

/* features */
.features{position:absolute;top:880px;left:200px;width:800px;display:flex;justify-content:space-between}
.feature{width:170px;text-align:center}
.feature-icon{width:80px;height:80px;border-radius:50%;background:var(--teal);margin:0 auto 14px;display:flex;align-items:center;justify-content:center}
.feature-name{font-size:17px;color:var(--ink);margin-bottom:8px}
.feature-text{font-size:11px;line-height:1.55;color:var(--muted);text-align:left}

/* bands */
.band-green{position:absolute;top:1150px;left:0;width:1200px;height:200px;
  background:linear-gradient(90deg,var(--teal) 0%,var(--green) 55%,var(--green-light) 100%);text-align:center;color:var(--white)}
.band-kicker{font-size:14px;letter-spacing:3px;padding-top:40px}
.band-title{font-size:42px;margin-top:4px}
.btn-white{background:var(--white);color:var(--ink);margin-top:12px;padding:9px 40px}

/* services */
.services{position:absolute;top:1600px;left:160px;width:880px;display:flex;justify-content:space-between}
.service{width:270px}
.service-photo{width:270px;height:180px;background:linear-gradient(135deg,#e4ecef,#b7cdd6)}
.service-title{font-size:20px;margin-top:16px;color:var(--ink)}
.service-text{font-size:11px;line-height:1.55;color:var(--muted);margin-top:6px}
.btn-teal{background:var(--teal);color:var(--white);margin-top:18px;padding:8px 26px;font-size:10px}

.band-photo{position:absolute;top:2050px;left:0;width:1200px;height:220px;
  background:linear-gradient(90deg,#5fb8ad 0%,#8ccfc4 50%,#6ec1b5 100%);text-align:center;color:var(--white)}
.band-photo .band-kicker{padding-top:46px;opacity:.8}
.btn-dark{background:var(--teal-dark);color:var(--white);margin-top:12px;padding:9px 36px}

/* footer */
.site-footer{position:absolute;top:2270px;left:0;width:1200px;height:230px;background:var(--footer);color:#c8d0d5}
.footer-inner{display:flex;padding:34px 48px 0;gap:60px}
.footer-brand{width:340px}
.footer-brand .brand-name{color:var(--white)}
.footer-about{font-size:11px;line-height:1.6;margin-top:16px;color:#9aa6ae}
.footer-col{width:190px;font-size:12px;line-height:1.75}
.footer-col h3{font-family:"Oswald",Arial,sans-serif;font-weight:400;font-size:17px;color:var(--green);text-transform:uppercase;letter-spacing:1px;margin-bottom:6px}
.footer-bar{position:absolute;bottom:0;left:0;width:1200px;height:30px;background:var(--footer-bar);text-align:center;font-size:10px;line-height:30px;color:#8a969e;letter-spacing:1px}
</style>
</head>
<body>

<section class="hero">
  <div class="hero-photo" role="img" aria-label="Smiling doctor in a white coat with a stethoscope, arms crossed, in a bright clinic"></div>
  <header class="site-header">
    <div class="brand"><span class="brand-mark"></span><span class="brand-name">Antigen Preservation Bureau</span></div>
    <nav class="nav">
      <span>Getting Started</span><span>Mentorship</span><span>Accelerate Your Goals</span><span>Questions</span><span class="nav-cta"></span>
    </nav>
  </header>
  <div class="hero-copy">
    <h1 class="heading hero-title">Find integrative health<br>services near you</h1>
    <p class="hero-text">We stabilize viruses, viral vectors and vaccines so they travel safely without the cold chain. Partner with our team for research, licensing and room temperature solutions.</p>
    <span class="btn btn-green">Shop All Menu</span>
  </div>
</section>

<h2 class="heading section-title" style="top:670px">Let's Talk About Us</h2>
<p class="section-lead" style="top:740px">Our scientists develop stabilization methods that keep biologics potent at room temperature. We work with pharmaceutical and therapeutic partners to bring vaccines to every region of the world.</p>

<div class="features">
  <div class="feature">
    <div class="feature-icon"><svg width="36" height="36" viewBox="0 0 36 36" fill="none" stroke="#fff" stroke-width="2.5"><path d="M8 28 C8 14 18 8 30 8 C30 20 24 28 10 28 Z"/><path d="M8 28 L20 16"/></svg></div>
    <div class="feature-name">Nutrition</div>
    <p class="feature-text">Balanced guidance built on research, helping each patient find a routine that lasts.</p>
  </div>
  <div class="feature">
    <div class="feature-icon"><svg width="36" height="36" viewBox="0 0 36 36" fill="none" stroke="#fff" stroke-width="2.5"><circle cx="18" cy="16" r="10"/><path d="M13 30 H23"/></svg></div>
    <div class="feature-name">Energy &amp; Mind</div>
    <p class="feature-text">Calm focus and steady energy through simple daily habits and expert support.</p>
  </div>
  <div class="feature">
    <div class="feature-icon"><svg width="36" height="36" viewBox="0 0 36 36" fill="none" stroke="#fff" stroke-width="2.5"><path d="M18 30 C6 22 6 10 12 8 C15 7 18 10 18 12 C18 10 21 7 24 8 C30 10 30 22 18 30 Z"/></svg></div>
    <div class="feature-name">Wellness</div>
    <p class="feature-text">Whole body care that connects prevention, treatment and recovery in one plan.</p>
  </div>
  <div class="feature">
    <div class="feature-icon"><svg width="36" height="36" viewBox="0 0 36 36" fill="none" stroke="#fff" stroke-width="2.5"><circle cx="18" cy="19" r="11"/><path d="M18 19 L18 12 M15 5 H21"/></svg></div>
    <div class="feature-name">Exercise</div>
    <p class="feature-text">Movement programs tailored to your level, designed to build strength over time.</p>
  </div>
</div>

<section class="band-green">
  <p class="heading band-kicker">Health and Nutritional Advice</p>
  <h2 class="heading band-title">Consultations and Group Workshops</h2>
  <span class="btn btn-white">Clinic Locator</span>
</section>

<h2 class="heading section-title" style="top:1410px">Let's Talk About Us</h2>
<p class="section-lead" style="top:1480px">From early formulation to final licensing, our team supports every step. We share stabilizing technology with partners who aim to reach patients far beyond the current cold chain.</p>

<div class="services">
  <div class="service">
    <div class="service-photo" role="img" aria-label="Doctor examining a patient in a clinic bed"></div>
    <h3 class="service-title">Maintaining Health</h3>
    <p class="service-text">Routine checks and clear advice that keep you well and help catch concerns early.</p>
    <span class="btn btn-teal">Appointment</span>
  </div>
  <div class="service">
    <div class="service-photo" role="img" aria-label="Physician consulting with a patient at a desk"></div>
    <h3 class="service-title">Maintaining Health</h3>
    <p class="service-text">Personal consultations with specialists who listen and plan care around your needs.</p>
    <span class="btn btn-teal">Appointment</span>
  </div>
  <div class="service">
    <div class="service-photo" role="img" aria-label="Medical team reviewing results on a laptop"></div>
    <h3 class="service-title">Maintaining Health</h3>
    <p class="service-text">Modern lab testing and reporting that give you answers quickly and in plain terms.</p>
    <span class="btn btn-teal">Appointment</span>
  </div>
</div>

<section class="band-photo" role="img" aria-label="Teal tinted photo of a clinical consultation behind the banner text">
  <p class="heading band-kicker">Health and Nutritional Advice</p>
  <h2 class="heading band-title">Consultations and Group Workshops</h2>
  <span class="btn btn-dark">Visit Our Showroom</span>
</section>

<footer class="site-footer">
  <div class="footer-inner">
    <div class="footer-brand">
      <div class="brand"><span class="brand-mark"></span><span class="brand-name">Antigen Preservation Bureau</span></div>
      <p class="footer-about">Research services that stabilize viruses, vectors and vaccines for safe global distribution.</p>
    </div>
    <div class="footer-col">
      <h3>Customer Service</h3>
      <p>Free Sample Shipping</p><p>30 Day Returns</p><p>Research Insurance</p><p>Terms &amp; Conditions</p>
    </div>
    <div class="footer-col">
      <h3>About Us</h3>
      <p>Top rating from Trade Council</p><p>Testimonials</p><p>Conflict Free Policy</p><p>Why Partner With Us</p>
    </div>
    <div class="footer-col">
      <h3>Contact Us</h3>
      <p>Email Us</p><p>(555) 014-2290</p><p>(555) 014-7731</p>
    </div>
  </div>
  <div class="footer-bar">© 2024 Antigen Preservation Bureau | 1219 Birch Street, Suite 100, Lakeview</div>
</footer>

</body>
</html>
```